I challenge you to create Denmark's coolest roofing company website

We need to have a website created for our roofing company.

I have some pages that can be used as a starting point because there are some things we would like to have, one important thing is a roof calculator, in addition to that information about the company, pictures of tasks we have completed, links to Friendlio and Pictavoro pages.

reviews from rated, etc. should also be visible on the page.

we have lots of pictures, videos, logos,

we need to have a nice home page that is just a little cooler than the competitors.
we need to steal their customer. the page should be easy and clear but with a nice design.
an important thing is the calculator.
come up with some suggestions we are quite open as long as it is a nice design
Updates

I have made an update in the PDF file with some thoughts and wishes. The file has been uploaded.

Target Market(s)

20-60

Industry/Entity Type

carpenter - roofer

Coding

Coded - Design and coding required

Number of Pages Required

4 page

Font styles to use
Sans Serif

Colors
EB3D1F
EC4F4E
F09395
F8D3D4
FCEDEE

Requirements
Must have
• Roof calculator, nice design, easy to get around
Nice to have
• the competitors : https://mollerbyghuset.dk https://hvid-tegl.dk https://strandbyghuset.dk

```html
<!DOCTYPE html>
<html lang="en">
<head>
<meta charset="utf-8">
<title>Tagmester Nord – Roofing</title>
<link href="https://fonts.googleapis.com/css2?family=Poppins:wght@400;500;600;700&display=swap" rel="stylesheet">
<style>
:root{
  --red:#D7202E;
  --red-soft:#EC4F4E;
  --pink:#FCEDEE;
  --pink-mid:#F8D3D4;
  --ink:#1d1d1f;
  --dark:#202022;
  --text:#555;
  --white:#fff;
}
*{margin:0;padding:0;box-sizing:border-box}
html,body{width:1200px;height:4396px;overflow:hidden}
body{font-family:"Poppins",sans-serif;color:var(--ink);background:var(--white);position:relative}
a{color:inherit;text-decoration:none}
.btn{display:inline-block;background:var(--red);color:var(--white);font-size:11px;font-weight:600;letter-spacing:.5px;padding:10px 22px;border-radius:3px;text-transform:uppercase}
.btn-dark{background:var(--ink)}
.section-title{font-size:34px;font-weight:600;text-align:center}
.section-title span{color:var(--red)}
.small{font-size:12px;line-height:1.6;color:var(--text)}

/* header */
.site-header{position:absolute;top:0;left:0;width:1200px;height:120px;background:var(--white)}
.logo{position:absolute;left:160px;top:34px;font-size:30px;font-weight:700;color:var(--red);display:flex;align-items:center;gap:10px}
.logo-mark{width:14px;height:14px;background:var(--red)}
.topbar{position:absolute;right:160px;top:10px;display:flex;gap:22px;align-items:center;font-size:12px;color:var(--ink)}
.topbar .social{display:flex;gap:10px}
.social i{display:block;width:14px;height:14px;border-radius:50%;background:var(--ink)}
.topbar .item{display:flex;align-items:center;gap:6px}
.topbar .item i{width:10px;height:10px;border-radius:50%;background:var(--red);display:block}
.main-nav{position:absolute;right:160px;top:60px;display:flex;align-items:center;gap:26px;font-size:13px;font-weight:500}
.main-nav .active{color:var(--red)}

/* hero */
.hero{position:absolute;top:120px;left:0;width:1200px;height:668px;overflow:hidden}
.hero-photo{position:absolute;inset:0;background:linear-gradient(180deg,#7da9d6 0%,#b9d1e6 30%,#55595e 55%,#2f3236 80%,#6b6b5c 100%)}
.hero-shapes{position:absolute;inset:0}
.hero-copy{position:absolute;left:160px;top:328px;color:var(--white);width:560px}
.hero-copy .eyebrow{font-size:11px;font-weight:600;letter-spacing:1px}
.hero-copy h1{font-size:44px;line-height:1.15;font-weight:700;margin:12px 0 12px}
.hero-copy p{font-size:13px;margin-bottom:26px}
.hero-arrows{position:absolute;right:12px;top:290px;display:flex;flex-direction:column;gap:28px}
.hero-arrows span{width:28px;height:28px;border-radius:50%;background:rgba(0,0,0,.55);display:block}

/* about */
.about{position:absolute;top:788px;left:0;width:1200px;height:520px}
.about-copy{position:absolute;left:160px;top:90px;width:420px}
.about-copy h2{font-size:34px;font-weight:600;margin-bottom:14px}
.about-copy h2 span{color:var(--red)}
.about-copy p{margin-bottom:24px}
.about-visual{position:absolute;left:660px;top:40px;width:420px;height:440px}
.about-photo{position:absolute;left:120px;top:40px;width:200px;height:400px;border-radius:100px 100px 0 0;background:linear-gradient(180deg,#7a5a44 0%,#c9a58c 40%,#2a2a2a 70%,#111 100%)}

/* services */
.services{position:absolute;top:1308px;left:0;width:1200px;height:604px;background:var(--pink)}
.services .section-title{margin-top:56px}
.card-row{position:absolute;left:160px;top:140px;display:flex;gap:20px}
.service-card{width:280px;height:324px;background:var(--white);text-align:center;border-radius:4px;overflow:hidden}
.service-img{height:176px}
.service-card h3{font-size:15px;font-weight:600;margin:16px 0 8px}
.service-card p{font-size:11px;line-height:1.5;color:var(--text);padding:0 34px}
.more{display:inline-block;margin-top:10px;font-size:10px;font-weight:600;color:var(--red);border-bottom:1px solid var(--red)}
.slider-arrow{position:absolute;top:282px;width:28px;height:28px;border-radius:50%;background:var(--white);box-shadow:0 2px 6px rgba(0,0,0,.15)}
.services .center-btn{position:absolute;top:530px;left:0;width:1200px;text-align:center}

/* why choose */
.why{position:absolute;top:1912px;left:0;width:1200px;height:448px;background:var(--dark);color:var(--white);text-align:center}
.why .section-title{margin-top:54px}
.features{position:absolute;top:150px;left:160px;width:880px;display:flex;justify-content:space-between}
.feature{width:270px}
.feature svg{display:block;margin:0 auto 12px}
.feature h3{font-size:15px;font-weight:600;margin-bottom:6px}
.feature p{font-size:12px;line-height:1.5;color:#ddd}
.why .center-btn{position:absolute;top:362px;left:0;width:1200px}

/* projects */
.projects{position:absolute;top:2360px;left:0;width:1200px;height:712px}
.projects .section-title{margin-top:48px}
.project-grid{position:absolute;left:32px;top:120px;width:1136px;display:grid;grid-template-columns:repeat(3,1fr);gap:20px 16px}
.project-grid div{height:240px}
.projects .center-btn{position:absolute;top:660px;left:0;width:1200px;text-align:center}

/* blog */
.blog{position:absolute;top:3072px;left:0;width:1200px;height:628px}
.blog .section-title{margin-top:50px}
.blog-row{position:absolute;left:160px;top:120px;display:flex;gap:20px}
.post{width:280px;height:428px;background:var(--white);box-shadow:0 3px 14px rgba(0,0,0,.1)}
.post-img{height:170px}
.post-meta{display:flex;gap:14px;margin:14px 16px 12px;font-size:10px;color:var(--text)}
.post-meta span{background:var(--pink);padding:4px 8px;border-radius:2px;display:flex;align-items:center;gap:5px}
.post-meta i{width:8px;height:8px;background:var(--red);border-radius:50%;display:block}
.post h3{font-size:15px;font-weight:600;line-height:1.3;margin:0 16px 10px}
.post p{font-size:11px;line-height:1.5;color:var(--text);margin:0 16px 16px}
.post .read{margin:0 16px;font-size:10px;font-weight:600}
.blog .center-btn{position:absolute;top:572px;left:0;width:1200px;text-align:center}

/* cta */
.cta{position:absolute;top:3700px;left:0;width:1200px;height:372px;text-align:center}
.cta h2{font-size:30px;font-weight:600;line-height:1.25;margin-top:64px}
.cta h2 span{color:var(--red)}
.cta p{width:700px;margin:16px auto 24px}

/* footer */
.site-footer{position:absolute;top:4072px;left:0;width:1200px;height:324px;background:#0d0d0d;color:var(--white)}
.footer-brand{position:absolute;left:200px;top:104px}
.footer-brand .logo{position:static;color:var(--white);font-size:28px}
.footer-brand .social{display:flex;gap:12px;margin:18px 0 0 40px}
.footer-brand .social i{background:var(--white)}
.foot-col{position:absolute;top:46px;font-size:12px}
.foot-col h4{font-size:15px;font-weight:600;margin-bottom:16px}
.foot-col li{list-style:none;margin-bottom:12px;color:#ddd}
.links{left:488px}
.links2{left:620px;top:80px}
.contact{left:776px;width:240px}
.contact li{display:flex;gap:10px;align-items:flex-start}
.contact li i{flex:none;width:14px;height:14px;border-radius:50%;background:var(--red);display:block;margin-top:2px}
.copyright{position:absolute;left:0;bottom:0;width:1200px;height:46px;border-top:1px solid #2c2c2c;text-align:center;font-size:11px;line-height:46px;color:#bbb}
</style>
</head>
<body>

<header class="site-header">
  <a class="logo" href="#"><span class="logo-mark"></span>Tagmester Nord</a>
  <div class="topbar">
    <div class="social"><i aria-label="Friendlio"></i><i aria-label="Pictavoro"></i><i aria-label="Video"></i></div>
    <div class="item"><i></i>555-010-2200</div>
    <div class="item"><i></i>kontakt@tagmesternord.dk</div>
  </div>
  <nav class="main-nav">
    <a class="active" href="#">Home</a>
    <a href="#">About</a>
    <a href="#">Services</a>
    <a href="#">Our Project</a>
    <a href="#">Blog</a>
    <a href="#">Contact Us</a>
    <a class="btn" href="#">Price Calculator</a>
  </nav>
</header>

<section class="hero">
  <div class="hero-photo" role="img" aria-label="House with a new dark tiled roof under a blue sky"></div>
  <svg class="hero-shapes" width="1200" height="668" viewBox="0 0 1200 668">
    <polygon points="0,668 0,180 620,40 880,668" fill="rgba(0,0,0,.35)"/>
    <polygon points="0,668 0,380 720,110 960,668" fill="#D7202E"/>
    <polygon points="720,110 960,668 1040,668" fill="#b01824"/>
  </svg>
  <div class="hero-copy">
    <div class="eyebrow">WELCOME TO TAGMESTER NORD</div>
    <h1>Protect Your Home with Expert Roofing Solutions</h1>
    <p>Free Estimates • Certified Roofers • Trusted Locally</p>
    <a class="btn btn-dark" href="#">Learn More</a>
  </div>
  <div class="hero-arrows"><span></span><span></span></div>
</section>

<section class="about">
  <div class="about-copy">
    <h2>About <span>Us</span></h2>
    <p class="small">Lorem Ipsum is simply dummy text of the printing and typesetting industry. Lorem Ipsum has been the industry's standard dummy text ever since the 1500s, when an unknown printer took a galley of type and scrambled it to make a type specimen book. It has survived not only five centuries but also the leap into electronic typesetting, remaining essentially unchanged. It was popularised in the 1960s with the release of transfer sheets containing Lorem Ipsum passages, and more recently with desktop publishing software that includes many versions of Lorem Ipsum.</p>
    <a class="btn" href="#">Learn More</a>
  </div>
  <div class="about-visual">
    <svg width="420" height="440" viewBox="0 0 420 440" style="position:absolute;left:0;top:0">
      <polygon points="0,440 150,200 260,440" fill="#D7202E"/>
      <polygon points="260,440 380,240 420,300 420,440" fill="#1d1d1f"/>
    </svg>
    <div class="about-photo" role="img" aria-label="Smiling team member of the roofing company"></div>
  </div>
</section>

<section class="services">
  <h2 class="section-title">Our <span>Services</span></h2>
  <div class="card-row">
    <article class="service-card">
      <div class="service-img" role="img" aria-label="New dark roof on a house" style="background:linear-gradient(160deg,#c7d3dc,#3b3e43 60%,#2a2c30)"></div>
      <h3>New Roof</h3>
      <p>It is a long established fact that a reader will be distracted by the looking at its layout.</p>
      <a class="more" href="#">SEE MORE</a>
    </article>
    <article class="service-card">
      <div class="service-img" role="img" aria-label="Roofers working on a roof" style="background:linear-gradient(170deg,#9fc4e4,#d9b46a 55%,#8a6a48)"></div>
      <h3>Acute Injuries</h3>
      <p>It is a long established fact that a reader will be distracted by the looking at its layout.</p>
      <a class="more" href="#">SEE MORE</a>
    </article>
    <article class="service-card">
      <div class="service-img" role="img" aria-label="Carpenter building roof framing" style="background:linear-gradient(170deg,#b9cbe0,#a88a6a 55%,#6d5a46)"></div>
      <h3>Carpenter</h3>
      <p>It is a long established fact that a reader will be distracted by the looking at its layout.</p>
      <a class="more" href="#">SEE MORE</a>
    </article>
  </div>
  <span class="slider-arrow" style="left:146px"></span>
  <span class="slider-arrow" style="left:1026px"></span>
  <div class="center-btn"><a class="btn" href="#">View All Services</a></div>
</section>

<section class="why">
  <h2 class="section-title">Why Choose Tagmester Nord</h2>
  <div class="features">
    <div class="feature">
      <svg width="42" height="42" viewBox="0 0 42 42" fill="none" stroke="#fff" stroke-width="2"><circle cx="21" cy="21" r="17"/><path d="M21 11v10l7 5"/></svg>
      <h3>Save Time And Money</h3>
      <p>Lorem Ipsum is simply dummy text of the printing and typesetting industry</p>
    </div>
    <div class="feature">
      <svg width="42" height="42" viewBox="0 0 42 42" fill="none" stroke="#fff" stroke-width="2"><path d="M12 14h18"/><path d="M14 14a7 7 0 0 1 14 0"/><circle cx="21" cy="20" r="5"/><path d="M8 40v-6a8 8 0 0 1 8-8h10a8 8 0 0 1 8 8v6"/></svg>
      <h3>Our Team Keeps It Clean</h3>
      <p>Lorem Ipsum is simply dummy text of the printing and typesetting industry</p>
    </div>
    <div class="feature">
      <svg width="42" height="42" viewBox="0 0 42 42" fill="none" stroke="#fff" stroke-width="2"><path d="M6 36h30V16L21 6 6 16z"/><path d="M12 20h18M12 26h18M12 32h18M17 16v20M25 16v20"/></svg>
      <h3>Technology On Your Side</h3>
      <p>Lorem Ipsum is simply dummy text of the printing and typesetting industry</p>
    </div>
  </div>
  <div class="center-btn"><a class="btn" href="#">Price Calculator</a></div>
</section>

<section class="projects">
  <h2 class="section-title">Our <span>Projects</span></h2>
  <div class="project-grid">
    <div role="img" aria-label="Brick house with red tiled roof" style="background:linear-gradient(170deg,#6aa3d8,#c9663d 55%,#8a4a30)"></div>
    <div role="img" aria-label="Timber roof framework from inside" style="background:linear-gradient(160deg,#8a6848,#c9a074 50%,#5a4230)"></div>
    <div role="img" aria-label="Yellow house with dark roof" style="background:linear-gradient(170deg,#a9c7e4,#2e3034 45%,#d2a74e)"></div>
    <div role="img" aria-label="Modern house with black roof" style="background:linear-gradient(170deg,#bcd3ea,#2b2d31 55%,#6f6f66)"></div>
    <div role="img" aria-label="Close-up of metal roof sheets" style="background:linear-gradient(160deg,#dfe5ea,#8b9198 50%,#3a3e44)"></div>
    <div role="img" aria-label="Dark roof tiles under blue sky" style="background:linear-gradient(170deg,#7fb0e0,#3a3c40 50%,#1f2023)"></div>
  </div>
  <div class="center-btn"><a class="btn" href="#">View All Projects</a></div>
</section>

<section class="blog">
  <h2 class="section-title">Our <span>Blog</span></h2>
  <div class="blog-row">
    <article class="post">
      <div class="post-img" role="img" aria-label="Roofer installing metal roofing" style="background:linear-gradient(170deg,#9cc3e6,#c4cbd2 50%,#6a6e74)"></div>
      <div class="post-meta"><span><i></i>Feb 10,2025</span><span><i></i>10 Comments</span></div>
      <h3>When To Seek Business For Your Advisory Support</h3>
      <p>It is a long established fact that a reader will be distracted by the looking at its layout.</p>
      <a class="read" href="#">LEARN MORE →</a>
    </article>
    <article class="post">
      <div class="post-img" role="img" aria-label="Roofers working on a roof in sunlight" style="background:linear-gradient(170deg,#f0b04a,#3f5e8c 55%,#2c3442)"></div>
      <div class="post-meta"><span><i></i>Feb 10,2025</span><span><i></i>10 Comments</span></div>
      <h3>When To Seek Business For Your Advisory Support</h3>
      <p>It is a long established fact that a reader will be distracted by the looking at its layout.</p>
      <a class="read" href="#">LEARN MORE →</a>
    </article>
    <article class="post">
      <div class="post-img" role="img" aria-label="Roofer laying panels on a roof" style="background:linear-gradient(170deg,#a7cbe8,#5d7596 55%,#3a4250)"></div>
      <div class="post-meta"><span><i></i>Feb 10,2025</span><span><i></i>10 Comments</span></div>
      <h3>When To Seek Business For Your Advisory Support</h3>
      <p>It is a long established fact that a reader will be distracted by the looking at its layout.</p>
      <a class="read" href="#">LEARN MORE →</a>
    </article>
  </div>
  <div class="center-btn"><a class="btn" href="#">View All Blog</a></div>
</section>

<section class="cta">
  <h2>Safeguard Your Property With<br>Trusted <span>Roofing Experts</span></h2>
  <p class="small">Lorem Ipsum Contracting, we know that remodeling your home can be a big decision. Our design process is proven to ensure a custom look tailored to your desire. We include our clients in every step of the design process. With state-of-the-art design software, you will be able to visualize your project before anything is installed. Your dream along with our expertise creates value that is built to last for years to come.</p>
  <a class="btn" href="#">Price Calculator</a>
</section>

<footer class="site-footer">
  <div class="footer-brand">
    <a class="logo" href="#"><span class="logo-mark"></span>Tagmester Nord</a>
    <div class="social"><i aria-label="Friendlio"></i><i aria-label="Pictavoro"></i><i aria-label="Video"></i></div>
  </div>
  <div class="foot-col links">
    <h4>Quick Links</h4>
    <ul><li>Home</li><li>About Us</li><li>Products</li><li>Our Services</li></ul>
  </div>
  <div class="foot-col links2">
    <ul><li>Testimonial</li><li>Contact Us</li></ul>
  </div>
  <div class="foot-col contact">
    <h4>Contact Us</h4>
    <ul>
      <li><i></i>(555) 010-3300</li>
      <li><i></i>kontakt@tagmesternord.dk</li>
      <li><i></i>14 Havnevej Suite 3,<br>Aarhus, Denmark</li>
    </ul>
  </div>
  <div class="copyright">© 2025 Copyright - Tagmester Nord. All Rights Reserved</div>
</footer>

</body>
</html>
```